Build a Wordpress Website for Brightvane

I need a wordpress website for brightvane, and facts that are update hourly.
So people who come to my website can browse through facts.
The website will be in english

Example is : brightvane.com

Give your best design and ideas.

NOTE: The Winner must deliver all files , PHP ,HTML , CSS , Javascript and other files , images etc. which are used for website.

```html
<!DOCTYPE html>
<html lang="en">
<head>
<meta charset="utf-8">
<title>Brightvane</title>
<link rel="stylesheet" href="https://fonts.googleapis.com/css2?family=Lobster&family=Open+Sans:ital,wght@0,400;0,600;0,700;1,400;1,700&family=Roboto:wght@500;700&display=swap">
<style>
:root{
  --brand:#5ef2a8;
  --white:#ffffff;
  --nav-bg:#0a0a0a;
  --nav-text:#c9c9c9;
  --card-bg:#ffffff;
  --card-title:#111111;
  --sky-top:#3a4656;
  --sky-mid:#6f7d8e;
  --sky-low:#b9a27a;
  --accent-pink:#f06aa0;
  --accent-gold:#ffd23f;
  --accent-green:#9be36b;
}
*{box-sizing:border-box;margin:0;padding:0}
html,body{width:1200px;height:631px;overflow:hidden}
body{position:relative;font-family:"Open Sans",sans-serif;color:var(--white)}
.site-backdrop{position:absolute;inset:0;
  background:radial-gradient(ellipse at 55% 100%,#f3c77a 0%,rgba(243,199,122,0) 45%),
  linear-gradient(180deg,var(--sky-top) 0%,var(--sky-mid) 30%,#56667a 55%,var(--sky-low) 100%)}
.site-header{position:absolute;top:0;left:0;width:1200px;height:161px;text-align:center}
.site-title{font-family:"Lobster",cursive;font-weight:400;font-size:62px;color:var(--brand);line-height:1;position:absolute;top:4px;left:0;width:100%}
.site-tagline{font-family:"Lobster",cursive;font-size:24px;color:var(--white);position:absolute;top:82px;left:0;width:100%}
.main-nav{position:absolute;top:161px;left:0;width:1200px;height:48px;background:var(--nav-bg);display:flex;align-items:center;padding-left:62px}
.main-nav svg{width:16px;height:16px;margin-right:38px}
.main-nav a{color:var(--nav-text);text-decoration:none;font-size:13.5px;margin-right:30px}
.main-nav a.current{color:var(--white)}
.fact-grid{position:absolute;top:229px;left:83px;width:1040px;height:402px;overflow:hidden;display:grid;grid-template-columns:repeat(4,251px);column-gap:11px;row-gap:36px}
.fact-card{background:var(--card-bg);height:311px;display:flex;flex-direction:column;box-shadow:0 1px 3px rgba(0,0,0,.4)}
.fact-media{position:relative;height:251px;overflow:hidden}
.fact-title{flex:1;display:flex;align-items:center;justify-content:center;text-align:center;font-family:"Roboto",sans-serif;font-weight:700;font-size:15px;color:var(--card-title);line-height:1.25;padding:0 10px}
.media-fill{position:absolute;inset:0}
.overlay{position:absolute;left:0;right:0;padding:0 12px;text-align:center;text-shadow:0 1px 3px rgba(0,0,0,.7)}
.lead{font-size:19px;line-height:1.2}
.small{font-size:9px;line-height:1.3;opacity:.9}
.source{position:absolute;right:8px;bottom:5px;font-size:6px;opacity:.8}
.hl-pink{color:var(--accent-pink)}
.hl-gold{color:var(--accent-gold)}
.mosq-head{position:absolute;top:6px;left:8px;font-size:18px;color:#fff}
.mosq-steps{position:absolute;top:42px;left:8px;right:8px;display:grid;grid-template-columns:1fr 1fr;column-gap:14px;row-gap:104px;font-size:7px;line-height:1.3;color:#fff}
.mosq-steps b{color:var(--accent-gold);font-weight:400;font-style:italic}
.row-two .fact-media{height:60px}
.tag-label{position:absolute;top:6px;font-size:11px;color:#fff}
</style>
</head>
<body>
<div class="site-backdrop" role="img" aria-label="Cloudy sky at sunset filled with hot air balloons"></div>

<header class="site-header">
  <h1 class="site-title">Brightvane</h1>
  <p class="site-tagline">From the world's best learning content</p>
</header>

<nav class="main-nav">
  <svg viewBox="0 0 16 16" aria-label="Home"><path d="M8 1 1 7.5h2V15h4v-4h2v4h4V7.5h2z" fill="#c9c9c9"/></svg>
  <a class="current" href="#">Home</a>
  <a href="#">Sample Page</a>
  <a href="#">Business</a>
  <a href="#">Design</a>
  <a href="#">Education</a>
</nav>

<main class="fact-grid">
  <article class="fact-card">
    <div class="fact-media">
      <div class="media-fill" role="img" aria-label="Nebula pillars in deep space" style="background:linear-gradient(160deg,#1b2a78 0%,#6a2c7a 45%,#c8612f 75%,#2a1a3a 100%)"></div>
      <div class="overlay" style="top:120px;background:rgba(0,0,0,.35);padding-top:6px;padding-bottom:8px">
        <p class="lead">The "<span class="hl-gold">Pillars of Creation</span>"<br>were probably <i>destroyed</i><br>6,000 years ago.</p>
        <p class="small" style="margin-top:10px">Due to the distance, we won't be able to see the destruction from Earth for <i>another 1,000 years</i>.</p>
      </div>
      <span class="source">Source: Starfield Journal</span>
    </div>
    <h2 class="fact-title">The Pillars of Creation Have Been Destroyed</h2>
  </article>

  <article class="fact-card">
    <div class="fact-media">
      <div class="media-fill" role="img" aria-label="Civet cat beside coffee beans and a cup of coffee" style="background:linear-gradient(170deg,#2f4a22 0%,#4f6a34 40%,#6b5a3a 75%,#3a2d1f 100%)"></div>
      <div class="overlay" style="top:26px;text-align:left">
        <p class="lead">The world's <b>most expensive</b><br><b class="hl-gold">coffee</b> is made with beans<br>extracted from civet poop.</p>
      </div>
      <p class="overlay small" style="bottom:14px">The coffee that is produced from these beans is called <i>kopi luwak</i>, or <i>civet coffee</i>.</p>
      <span class="source">Source: Bean Ledger</span>
    </div>
    <h2 class="fact-title">Crappy Cups of Coffee</h2>
  </article>

  <article class="fact-card">
    <div class="fact-media">
      <div class="media-fill" role="img" aria-label="Vintage portrait of an industrialist over an oil refinery" style="background:linear-gradient(180deg,#c9a39a 0%,#b58d86 35%,#6f7b8a 70%,#3f5872 100%)"></div>
      <div class="overlay" style="top:175px">
        <p style="font-size:15px;line-height:1.25">"Don't be afraid to give up the good to go for <b>the great</b>."</p>
        <p style="font-size:10px;margin-top:8px;text-align:right">– Harold W. Ashcombe</p>
      </div>
    </div>
    <h2 class="fact-title">Oil Tycoon Harold W. Ashcombe</h2>
  </article>

  <article class="fact-card">
    <div class="fact-media">
      <div class="media-fill" role="img" aria-label="Close-up of a mosquito biting skin" style="background:linear-gradient(180deg,#5c6b3a 0%,#8a7a4a 40%,#d08b72 60%,#c5786a 100%)"></div>
      <p class="mosq-head">How Do Mosquitos <span style="background:#222;padding:0 3px">Bite</span>?</p>
      <div class="mosq-steps">
        <p>1. Mouthparts ending in <b>barbed blades</b> pierce the skin and anchor the mosquito</p>
        <p>2. Flexible mouthparts <b>probe</b> for a blood vessel, often for full minutes</p>
        <p>3. The mosquito deposits anticoagulant saliva while sucking up blood</p>
        <p>4. Mosquitos drink for <b>four minutes</b> on average</p>
      </div>
      <span class="source">Source: Wildline Review</span>
    </div>
    <h2 class="fact-title">Mosquito Mouths Aren't Just Big Needles</h2>
  </article>

  <article class="fact-card row-two">
    <div class="fact-media"><div class="media-fill" role="img" aria-label="Vintage portrait photograph" style="background:linear-gradient(180deg,#9fb3c4,#6c7f90)"></div></div>
  </article>
  <article class="fact-card row-two">
    <div class="fact-media"><div class="media-fill" role="img" aria-label="Small gliding animal on a branch" style="background:linear-gradient(180deg,#7a6f8a,#b8b0c4)"></div></div>
  </article>
  <article class="fact-card row-two">
    <div class="fact-media">
      <div class="media-fill" role="img" aria-label="Elephants on the savanna" style="background:linear-gradient(180deg,#2f6fb2,#3f82c4)"></div>
      <p class="overlay" style="top:8px;text-align:left;font-size:13px;line-height:1.3"><b>The Samburu people</b> of Kenya believe God created men and elephants as brothers.</p>
    </div>
  </article>
  <article class="fact-card row-two">
    <div class="fact-media">
      <div class="media-fill" role="img" aria-label="Baboons and bear cubs in the wild" style="background:linear-gradient(90deg,#6f6a4a 0 49%,#fff 49% 51%,#5a6a3f 51%)"></div>
      <span class="tag-label" style="left:40px">Baboons</span>
      <span class="tag-label" style="left:150px">Bear Cubs</span>
    </div>
  </article>
</main>
</body>
</html>
```